Banner Ad Design Project

We need a Banner to hang outside our Health Food Store to advertise to the public that we will be holding an Organic Market Day every Saturday.
We have our Business name and logo that will need to be incorporated into the design.
We want the design to convey freshness and have an earthy / farm feel, but also want the design to be crisp and not "Hippie"
we also need the banner to say "Fresh Organic Market every Saturday"
we will be selling fresh organic fruit and vegetables.
Target Market(s)
existing customers and general public walking past the shop
Industry/Entity Type
Farm
Look and feel

```html
<!DOCTYPE html>
<html lang="en">
<head>
<meta charset="utf-8">
<title>Harrowfield Wholefoods Store – Fresh Organic Market Every Saturday</title>
<link rel="stylesheet" href="https://fonts.googleapis.com/css2?family=Francois+One&family=Marck+Script&display=swap">
<style>
  :root {
    --linen-light: #e6d8c0;
    --linen: #dccab0;
    --linen-dark: #cdb896;
    --brand-brown: #b04e26;
    --script-green: #1d8f3c;
    --headline-ink: #1e1a17;
    --rule-ink: #2a2420;
    --apple-light: #c8202a;
    --apple-dark: #6e0a12;
  }
  html, body {
    margin: 0;
    padding: 0;
    overflow: hidden;
    background: var(--linen);
  }
  .banner {
    position: relative;
    width: 1200px;
    height: 720px;
    overflow: hidden;
    background: radial-gradient(ellipse at 45% 40%, var(--linen-light) 0%, var(--linen) 55%, var(--linen-dark) 100%);
    font-family: "Francois One", sans-serif;
  }
  .brand {
    position: absolute;
    left: 48px;
    top: 38px;
    color: var(--brand-brown);
    font-family: "Francois One", sans-serif;
    font-weight: 400;
    line-height: 0.95;
    text-transform: lowercase;
  }
  .brand-line-top {
    display: block;
    font-size: 72px;
    letter-spacing: 1px;
  }
  .brand-line-bottom {
    display: block;
    margin-top: 30px;
    font-size: 92px;
    letter-spacing: 0;
  }
  .produce-photo {
    position: absolute;
    left: 727px;
    top: 36px;
    width: 473px;
    height: 300px;
  }
  .script {
    position: absolute;
    left: 0;
    width: 100%;
    text-align: center;
    color: var(--script-green);
    font-family: "Marck Script", cursive;
    font-weight: 400;
    line-height: 1;
  }
  .script-fresh {
    top: 280px;
    padding-left: 150px;
    box-sizing: border-box;
    font-size: 96px;
  }
  .script-day {
    top: 560px;
    padding-left: 24px;
    box-sizing: border-box;
    font-size: 112px;
    letter-spacing: 3px;
  }
  .rule {
    position: absolute;
    left: 57px;
    width: 1086px;
    background: var(--rule-ink);
  }
  .rule-top-thick { top: 392px; height: 3px; }
  .rule-top-thin { top: 402px; height: 1px; }
  .rule-bottom-thin { top: 551px; height: 1px; }
  .rule-bottom-thick { top: 558px; height: 3px; }
  .headline {
    position: absolute;
    left: 0;
    top: 408px;
    width: 100%;
    margin: 0;
    text-align: center;
    color: var(--headline-ink);
    font-family: "Francois One", sans-serif;
    font-weight: 400;
    font-size: 128px;
    line-height: 1;
    letter-spacing: 9px;
    text-shadow: 2px 2px 0 rgba(255, 255, 255, 0.6);
  }
</style>
</head>
<body>
  <main class="banner">
    <div class="brand" aria-label="Harrowfield Wholefoods Store">
      <span class="brand-line-top">harrowfield</span>
      <span class="brand-line-bottom">wholefoods store</span>
    </div>

    <svg class="produce-photo" role="img" aria-label="Photograph of two shiny red apples" viewBox="0 0 473 300">
      <defs>
        <radialGradient id="apple-shade" cx="35%" cy="30%" r="75%">
          <stop offset="0%" stop-color="var(--apple-light)"/>
          <stop offset="100%" stop-color="var(--apple-dark)"/>
        </radialGradient>
      </defs>
      <ellipse cx="150" cy="160" rx="125" ry="125" fill="url(#apple-shade)"/>
      <ellipse cx="345" cy="160" rx="135" ry="140" fill="url(#apple-shade)"/>
    </svg>

    <div class="script script-fresh">Fresh</div>

    <div class="rule rule-top-thick"></div>
    <div class="rule rule-top-thin"></div>
    <h1 class="headline">ORGANIC MARKET</h1>
    <div class="rule rule-bottom-thin"></div>
    <div class="rule rule-bottom-thick"></div>

    <div class="script script-day">Every Saturday</div>
  </main>
</body>
</html>
```